Business Card Design Project for Investment Fund

Orvanel Asset Partners is an emerging wealth management firm based in New Jersey. It offers superior investment returns to high net worth individuals and institutions by finding undervalued assets.
We recently selected a company logo which was inspired by the Tucana constellation. Beta Tucanae is a group of six stars, containing star cluster 47 Tucanae, rated the second brightest object in the sky.
Now we need a business card design. Since we are an investment firm, the design should project a sense of stability, growth and professionalism. The owner is interested in something simple yet striking, which of course is consistent with the logo.
Target Market(s)
Wealthy individuals, probably middle aged or older, in the US
Industry/Entity Type
Investment

```html
<!DOCTYPE html>
<html lang="en">
<head>
<meta charset="utf-8">
<title>Orvanel Asset Partners — Business Card</title>
<link rel="stylesheet" href="https://fonts.googleapis.com/css2?family=Arimo:wght@400;700&display=swap">
<style>
  :root {
    --page-bg: #ffffff;
    --label: #2f3560;
    --divider: #eef3f8;
    --navy-deep: #262d58;
    --navy: #2d3766;
    --navy-bright: #33407e;
    --panel-light: #dcdbe6;
    --panel-mid: #c6c5d5;
    --panel-dark: #9f9db6;
    --ink: #26262e;
    --white: #ffffff;
    --mark: #1c2a8a;
  }
  * { margin: 0; padding: 0; box-sizing: border-box; }
  html, body {
    width: 1200px; height: 2172px; overflow: hidden;
    background: var(--page-bg);
    font-family: "Arimo", Arial, sans-serif;
  }
  .canvas { position: relative; width: 1200px; height: 2172px; }

  .side-label {
    position: absolute; left: 0; width: 1200px; text-align: center;
    font-size: 42px; color: var(--label);
  }
  .side-label--front { top: 100px; }
  .side-label--back { top: 904px; }

  .page-divider {
    position: absolute; left: 0; top: 1182px; width: 1200px; height: 3px;
    background: var(--divider);
  }

  /* Front */
  .card-front {
    position: absolute; left: 64px; top: 235px; width: 1077px; height: 615px;
    overflow: hidden;
    background: linear-gradient(90deg, var(--navy) 0%, var(--navy-deep) 50%, var(--navy-bright) 100%);
  }
  .card-front .panel {
    position: absolute; left: 0; top: 76px; width: 1077px; height: 463px;
    border-radius: 0 100px 0 100px;
    background: linear-gradient(90deg, var(--panel-dark) 0%, var(--panel-mid) 45%, var(--panel-light) 75%, var(--panel-light) 100%);
    box-shadow: 0 10px 24px rgba(10, 14, 40, 0.45);
  }
  .brand {
    position: absolute; left: 0; top: 176px; width: 1077px; text-align: center;
    color: var(--ink); font-weight: 700;
  }
  .brand-square {
    display: block; margin: 0 auto 28px; width: 158px; height: 158px;
    border-radius: 22px; background: var(--mark);
  }
  .brand-name { display: block; font-size: 58px; letter-spacing: 10px; line-height: 1; }
  .brand-sub { display: block; font-size: 30px; line-height: 1.4; margin-top: 4px; }

  /* Back */
  .card-back {
    position: absolute; left: 309px; top: 999px; width: 600px; height: 1051px;
    overflow: hidden;
    background: linear-gradient(180deg, var(--navy) 0%, var(--navy-deep) 100%);
  }
  .card-back .panel {
    position: absolute; left: 0; top: 74px; width: 600px; height: 901px;
    border-radius: 98px 0 0 98px;
    background: linear-gradient(180deg, var(--navy-deep) 0%, var(--navy) 40%, var(--navy-bright) 100%);
    box-shadow: -6px 10px 24px rgba(10, 14, 40, 0.5);
  }
  .name-band {
    position: absolute; left: 0; top: 363px; width: 600px; height: 161px;
    background: linear-gradient(90deg, var(--navy-bright) 0%, #2f3a72 60%, var(--navy-deep) 100%);
    box-shadow: 0 6px 14px rgba(10, 14, 40, 0.4);
  }
  .contact { position: absolute; left: 56px; color: var(--white); }
  .contact-name { top: 390px; font-size: 49px; font-weight: 700; letter-spacing: -0.5px; }
  .contact-title { top: 450px; font-size: 37px; }
  .contact-address { top: 563px; font-size: 31px; line-height: 41px; }
  .contact-email { top: 674px; font-size: 31px; font-weight: 700; }
  .contact-phone { top: 723px; font-size: 31px; font-weight: 700; }
  .contact-web { top: 804px; font-size: 31px; }
</style>
</head>
<body>
<main class="canvas">
  <div class="side-label side-label--front">Front</div>

  <section class="card-front" aria-label="Business card front">
    <div class="panel"></div>
    <div class="brand">
      <span class="brand-square" aria-hidden="true"></span>
      <span class="brand-name">ORVANEL</span>
      <span class="brand-sub">Asset Partners</span>
    </div>
  </section>

  <div class="side-label side-label--back">Back</div>
  <div class="page-divider"></div>

  <section class="card-back" aria-label="Business card back">
    <div class="panel"></div>
    <div class="name-band"></div>
    <div class="contact contact-name">Dana Holloway</div>
    <div class="contact contact-title">CEO</div>
    <div class="contact contact-address">88 Market St.<br>Hoboken, NJ 07030</div>
    <div class="contact contact-email">dholloway@orvanelap.com</div>
    <div class="contact contact-phone">201-555-0184</div>
    <div class="contact contact-web">www.orvanelap.com</div>
  </section>
</main>
</body>
</html>
```